Business Card Design Project

Velvet Harbor is a Boutique Clothing. On the business cards I would like to have this included
Website: www.velvetharbor-example.com
Email: shop@velvetharbor-example.com
Owner: Mira Sol & Tor Dell

Industry/Entity Type

Business

Contact Information for Business Card

I wanted something simple and elegant. I have attach business logo.

```html
<!DOCTYPE html>
<html lang="en">
<head>
<meta charset="UTF-8">
<title>Velvet Harbor — Business Card</title>
<link href="https://fonts.googleapis.com/css2?family=Open+Sans:wght@300;400;600;700&display=swap" rel="stylesheet">
<style>
  :root {
    --backdrop: #2e2a28;
    --card: #141414;
    --card-edge: #0b0b0b;
    --silver: #b9b9b9;
    --white: #f4f4f4;
    --muted: #d6d6d6;
    --rule: #6a6a6a;
  }
  * { margin: 0; padding: 0; box-sizing: border-box; }
  html, body {
    width: 1200px; height: 780px; overflow: hidden;
    background: var(--backdrop);
    font-family: "Open Sans", Arial, sans-serif;
  }
  .canvas {
    position: relative; width: 1200px; height: 780px;
    display: flex; align-items: center; justify-content: center; gap: 40px;
  }
  .card {
    position: relative; width: 540px; height: 309px;
    background: var(--card);
    border: 1px solid var(--card-edge);
    box-shadow: 0 10px 30px rgba(0,0,0,.45);
  }
  .brand {
    display: flex; flex-direction: column; align-items: center; gap: 14px;
    font-weight: 300; text-transform: uppercase; letter-spacing: 0.32em;
    text-align: center; line-height: 1.5;
  }
  .brand-dot {
    width: 64px; height: 64px; border-radius: 50%;
    border: 1.5px solid currentColor;
  }
  .card-front .brand {
    position: absolute; left: 50%; top: 50%; transform: translate(-50%, -50%);
    color: var(--silver); font-size: 19px;
  }
  .card-back .brand {
    position: absolute; left: 200px; top: 50%; transform: translate(-50%, -50%);
    color: var(--white); font-size: 15px; gap: 12px;
  }
  .card-back .brand-dot { width: 52px; height: 52px; }
  .divider {
    position: absolute; left: 292px; top: 92px; width: 1px; height: 125px;
    background: var(--rule);
  }
  .contact {
    position: absolute; left: 320px; top: 100px; color: var(--white);
  }
  .owners-name { font-size: 15px; font-weight: 700; letter-spacing: 0.01em; }
  .owners-role { font-size: 11px; font-weight: 400; color: var(--muted); margin-top: 1px; }
  .contact-list { list-style: none; margin-top: 14px; display: flex; flex-direction: column; gap: 8px; }
  .contact-item { display: flex; align-items: center; gap: 9px; font-size: 12px; }
  .contact-icon { width: 17px; height: 17px; flex: none; }
</style>
</head>
<body>
  <main class="canvas">
    <section class="card card-front" aria-label="Card front">
      <div class="brand">
        <span class="brand-dot" aria-hidden="true"></span>
        <span class="brand-name">Velvet<br>Harbor</span>
      </div>
    </section>

    <section class="card card-back" aria-label="Card back">
      <div class="brand">
        <span class="brand-dot" aria-hidden="true"></span>
        <span class="brand-name">Velvet<br>Harbor</span>
      </div>
      <div class="divider"></div>
      <div class="contact">
        <p class="owners-name">Mira Sol &amp; Tor Dell</p>
        <p class="owners-role">Owners</p>
        <ul class="contact-list">
          <li class="contact-item">
            <svg class="contact-icon" viewBox="0 0 20 20" fill="none" stroke="#f4f4f4" stroke-width="1.2" aria-hidden="true">
              <circle cx="10" cy="10" r="9"/>
              <circle cx="10" cy="10" r="5.5"/>
              <ellipse cx="10" cy="10" rx="2.4" ry="5.5"/>
              <line x1="4.5" y1="10" x2="15.5" y2="10"/>
            </svg>
            <span>www.velvetharbor-example.com</span>
          </li>
          <li class="contact-item">
            <svg class="contact-icon" viewBox="0 0 20 20" fill="none" stroke="#f4f4f4" stroke-width="1.2" aria-hidden="true">
              <circle cx="10" cy="10" r="9"/>
              <rect x="5" y="6.5" width="10" height="7" rx="0.6"/>
              <polyline points="5,7 10,11 15,7"/>
            </svg>
            <span>shop@velvetharbor-example.com</span>
          </li>
        </ul>
      </div>
    </section>
  </main>
</body>
</html>
```